Tarrow Creek plumbing plumbing company business card design

Something sinilar to business card i upload it is my old business card design
And have a good watermark with the logo or majority of the logot in rhe background as watermark

Plumbing business similar to uploaded design with a nice watermark of the logo

Font styles to use
Script

Colors

Designer to choose colors to be used in the design.

```html
<!DOCTYPE html>
<html lang="en">
<head>
<meta charset="utf-8">
<title>Tarrow Creek Plumbing — Business Card</title>
<link href="https://fonts.googleapis.com/css2?family=Montserrat:wght@400;600;700&display=swap" rel="stylesheet">
<style>
  :root{
    --backdrop:#32373e;
    --card-dark:#050606;
    --card-blue:#0078c1;
    --brand-blue:#1a86cf;
    --white:#ffffff;
    --faint-dark:rgba(255,255,255,0.07);
    --faint-blue:rgba(255,255,255,0.09);
  }
  *{box-sizing:border-box;margin:0;padding:0}
  html,body{width:1200px;height:1200px;overflow:hidden;background:var(--backdrop)}
  body{position:relative;font-family:'Montserrat',sans-serif;color:var(--white)}
  .card{position:absolute;left:290px;width:620px;height:354px;overflow:hidden;box-shadow:0 6px 18px rgba(0,0,0,.35)}
  .card--back{top:190px;background:var(--card-dark)}
  .card--front{top:620px;background:var(--card-blue)}

  .watermark{position:absolute;border-radius:50%}
  .card--back .watermark{width:300px;height:300px;left:-70px;top:120px;background:var(--faint-dark)}
  .card--front .watermark{width:320px;height:320px;right:-60px;top:-40px;background:var(--faint-blue)}

  .brand{position:absolute;display:flex;align-items:center;gap:12px}
  .brand__dot{width:22px;height:22px;border-radius:50%;background:var(--brand-blue);flex:none}
  .brand__name{font-weight:700;letter-spacing:.12em;text-transform:uppercase;line-height:1.15}
  .card--back .brand{left:175px;top:140px}
  .card--back .brand__name{font-size:24px;color:var(--white)}
  .card--front .brand{left:36px;top:52px}
  .card--front .brand__dot{background:var(--white)}
  .card--front .brand__name{font-size:22px;color:#050606}

  .web{position:absolute;right:40px;bottom:34px;font-size:12px;letter-spacing:.14em}

  .person{position:absolute;right:44px;top:120px;text-align:right}
  .person__name{font-size:30px;font-weight:600;letter-spacing:.05em}
  .person__role{font-size:14px;font-weight:600;margin-top:2px}

  .contact{position:absolute;left:40px;bottom:34px;display:flex;align-items:stretch;gap:12px}
  .contact__icons{display:flex;flex-direction:column;justify-content:space-around;gap:8px;padding:4px 0}
  .contact__icons svg{width:14px;height:14px;fill:var(--white)}
  .contact__rule{width:1px;background:var(--white)}
  .contact__list{list-style:none;font-size:12px;line-height:1.6;letter-spacing:.04em}
  .contact__list .phone{font-weight:700;font-size:13px;letter-spacing:.08em}
</style>
</head>
<body>
  <section class="card card--back" aria-label="Card back">
    <div class="watermark"></div>
    <div class="brand">
      <span class="brand__dot"></span>
      <span class="brand__name">Tarrow Creek<br>Plumbing</span>
    </div>
    <p class="web">www.tarrowcreekplumbing.com.au</p>
  </section>

  <section class="card card--front" aria-label="Card front">
    <div class="watermark"></div>
    <div class="brand">
      <span class="brand__dot"></span>
      <span class="brand__name">Tarrow Creek<br>Plumbing</span>
    </div>
    <div class="person">
      <p class="person__name">Daniel Vostrik</p>
      <p class="person__role">Director</p>
    </div>
    <div class="contact">
      <div class="contact__icons">
        <svg viewBox="0 0 24 24" aria-hidden="true"><path d="M6.6 10.8a15 15 0 0 0 6.6 6.6l2.2-2.2a1 1 0 0 1 1-.25 11.4 11.4 0 0 0 3.6.57 1 1 0 0 1 1 1V20a1 1 0 0 1-1 1A17 17 0 0 1 3 4a1 1 0 0 1 1-1h3.5a1 1 0 0 1 1 1c0 1.25.2 2.45.57 3.57a1 1 0 0 1-.25 1z"/></svg>
        <svg viewBox="0 0 24 24" aria-hidden="true"><path d="M2 11 22 2l-9 20-2-9z"/></svg>
        <svg viewBox="0 0 24 24" aria-hidden="true"><path d="M12 2a10 10 0 1 0 0 20 10 10 0 0 0 0-20zm0 2c1 1.2 1.8 3 2.1 5H9.9C10.2 7 11 5.2 12 4zM4.3 13a8 8 0 0 1 0-2h3.6a17 17 0 0 0 0 2zm.8 2h3.1c.3 1.5.8 2.8 1.5 3.9A8 8 0 0 1 5.1 15zm3.1-6H5.1a8 8 0 0 1 4.6-3.9C9 6.2 8.5 7.5 8.2 9zM12 20c-1-1.2-1.8-3-2.1-5h4.2c-.3 2-1.1 3.8-2.1 5zm2.3-7H9.7a15 15 0 0 1 0-2h4.6a15 15 0 0 1 0 2zm0 5.9c.7-1.1 1.2-2.4 1.5-3.9h3.1a8 8 0 0 1-4.6 3.9zM16.1 13a17 17 0 0 0 0-2h3.6a8 8 0 0 1 0 2zm-.3-4c-.3-1.5-.8-2.8-1.5-3.9A8 8 0 0 1 18.9 9z"/></svg>
      </div>
      <span class="contact__rule"></span>
      <ul class="contact__list">
        <li class="phone">0400 512 378</li>
        <li>info@tarrowcreekplumbing.com</li>
        <li>www.tarrowcreekplumbing.com.au</li>
        <li>Lic No. 480271c</li>
      </ul>
    </div>
  </section>
</body>
</html>
```